web design needed for jewellery inspired temporary tattoo company

Hi There

I need a web design for a new company I'm launching called coral glow luxe
Im a retailer of flash tattoos - temporary gold and silver metallic tattoos

These are the next new craze with many celebrities already displaying them whilst being lapped on their holidays

i need a very classy upmarket wow web design with an e commerce shop attached

I also offer marlow q bronze mist so will need a page to link to where people can get a tan and tattoo - so maybe as a box on the main page

As A guide I'm looking for someone to put their unique spin on an american website which is currently selling the same type of product
www.glintmarkz.com

the final design should oozzzz 'rich list ' coral luxe - think st tropez Monaco and needs to be linked to all my social media

please seepintrest flash tattoos for what we sell
I've attached my logo

I can't wait to hear from you all
many Thanks

Fiona Dembrey
www.coralglowluxe.co.uk

Target Market(s)

20 to 30's young party rich list glamous girls - festival boho cool beach LA

Industry/Entity Type

It Company

Number of Pages Required

3 page

Font styles to use
Script

Requirements
Must have
• a beach feel
• pictures of people wearing the tattoos
• an ecommerce site
• be easy to navigate
• my logo
• the wow factor
Nice to have
• a really classy expensive feel to the website
Should not have
• a cheap plain look

```html
<!DOCTYPE html>
<html lang="en">
<head>
<meta charset="utf-8">
<title>Most popular metallic tattoos</title>
<link rel="stylesheet" href="https://fonts.googleapis.com/css2?family=Open+Sans:wght@300;400;700&display=swap">
<style>
  :root {
    --bg: #ffffff;
    --ink: #1f1f1f;
    --name: #a9a9a9;
    --price: #444444;
    --rule: #d9d9d9;
    --gold: #c99a2e;
    --shade: rgba(45, 45, 45, 0.55);
    --tan: #9a5f3c;
    --sky: #b9c9c6;
    --cream: #f6f1e1;
    --forest: #4a4a3e;
  }
  * { margin: 0; padding: 0; box-sizing: border-box; }
  html, body {
    width: 1200px;
    height: 732px;
    overflow: hidden;
    background: var(--bg);
    font-family: "Open Sans", Arial, sans-serif;
  }
  .popular {
    position: relative;
    width: 1200px;
    height: 732px;
    padding: 0 30px;
  }
  .popular-title {
    text-align: center;
    font-size: 51px;
    font-weight: 300;
    letter-spacing: -1.5px;
    color: var(--ink);
    line-height: 1;
    padding-top: 16px;
  }
  .popular-title strong { font-weight: 700; }
  .product-grid {
    position: absolute;
    top: 123px;
    left: 30px;
    display: grid;
    grid-template-columns: repeat(4, 259px);
    column-gap: 35px;
    row-gap: 46px;
  }
  .product-card { text-align: center; }
  .product-photo {
    position: relative;
    width: 259px;
    height: 179px;
  }
  .photo-back-beach { background: linear-gradient(180deg, var(--sky) 0%, #d2ccbc 45%, var(--tan) 60%, #7d4a2c 100%); }
  .photo-ankle { background: linear-gradient(90deg, #3d3a36 0%, #8a5a3a 25%, #b07a52 55%, #5e564c 80%, #38352f 100%); }
  .photo-back-cream { background: linear-gradient(90deg, var(--cream) 0%, #c9895e 25%, #b1714a 55%, #d29a70 80%, var(--cream) 100%); }
  .photo-arms { background: linear-gradient(135deg, #3e3b37 0%, #b8805a 35%, #c89168 60%, var(--forest) 100%); }
  .hover-shade {
    position: absolute;
    inset: 0;
    background: var(--shade);
  }
  .cart-button {
    position: absolute;
    left: 98px;
    top: 58px;
    width: 62px;
    height: 62px;
    border-radius: 50%;
    background: var(--bg);
    display: flex;
    align-items: center;
    justify-content: center;
  }
  .product-name {
    margin-top: 16px;
    font-size: 33px;
    font-weight: 300;
    letter-spacing: -0.6px;
    line-height: 40px;
    color: var(--name);
  }
  .product-price {
    margin-top: 7px;
    font-size: 16px;
    line-height: 20px;
    letter-spacing: 0.2px;
    color: var(--price);
  }
  .price-old {
    margin-left: 24px;
    text-decoration: line-through;
  }
  .section-rule {
    position: absolute;
    left: 30px;
    right: 30px;
    top: 718px;
    border: 0;
    border-top: 1px solid var(--rule);
  }
</style>
</head>
<body>
<section class="popular">
  <h1 class="popular-title">Most popular <strong>metallic tattoos</strong></h1>

  <div class="product-grid">
    <article class="product-card">
      <div class="product-photo photo-back-beach" role="img" aria-label="Woman at the beach wearing a gold metallic tattoo down her spine"></div>
      <h2 class="product-name">Rosalinde</h2>
      <p class="product-price"><span class="price-now">$22.00</span><span class="price-old">$28.00</span></p>
    </article>

    <article class="product-card">
      <div class="product-photo photo-ankle" role="img" aria-label="Ankle wearing a silver flower chain metallic tattoo">
        <div class="hover-shade"></div>
        <a class="cart-button" href="#" aria-label="Add to bag">
          <svg width="26" height="24" viewBox="0 0 26 24" aria-hidden="true">
            <path d="M8 9 V6 a5 5 0 0 1 10 0 V9" fill="none" stroke="var(--gold)" stroke-width="2.4"/>
            <path d="M2 8 H24 L21.5 23 H4.5 Z" fill="var(--gold)"/>
            <path d="M6 12 H20" stroke="var(--bg)" stroke-width="1.2"/>
          </svg>
        </a>
      </div>
      <h2 class="product-name">Spirit of sea</h2>
      <p class="product-price"><span class="price-now">$22.00</span><span class="price-old">$28.00</span></p>
    </article>

    <article class="product-card">
      <div class="product-photo photo-back-cream" role="img" aria-label="Seated woman with a gold spine tattoo and arm cuff"></div>
      <h2 class="product-name">Coastal Roamer</h2>
      <p class="product-price"><span class="price-now">$22.00</span><span class="price-old">$28.00</span></p>
    </article>

    <article class="product-card">
      <div class="product-photo photo-arms" role="img" aria-label="Arms and legs wearing ornate gold metallic tattoos"></div>
      <h2 class="product-name">Amarella</h2>
      <p class="product-price"><span class="price-now">$22.00</span><span class="price-old">$28.00</span></p>
    </article>

    <article class="product-card">
      <div class="product-photo photo-back-beach" role="img" aria-label="Woman at the beach wearing a gold metallic tattoo down her spine"></div>
      <h2 class="product-name">Rosalinde</h2>
      <p class="product-price"><span class="price-now">$22.00</span><span class="price-old">$28.00</span></p>
    </article>

    <article class="product-card">
      <div class="product-photo photo-ankle" role="img" aria-label="Ankle wearing a silver flower chain metallic tattoo"></div>
      <h2 class="product-name">Spirit of sea</h2>
      <p class="product-price"><span class="price-now">$22.00</span><span class="price-old">$28.00</span></p>
    </article>

    <article class="product-card">
      <div class="product-photo photo-back-cream" role="img" aria-label="Seated woman with a gold spine tattoo and arm cuff"></div>
      <h2 class="product-name">Coastal Roamer</h2>
      <p class="product-price"><span class="price-now">$22.00</span><span class="price-old">$28.00</span></p>
    </article>

    <article class="product-card">
      <div class="product-photo photo-arms" role="img" aria-label="Arms and legs wearing ornate gold metallic tattoos"></div>
      <h2 class="product-name">Amarella</h2>
      <p class="product-price"><span class="price-now">$22.00</span><span class="price-old">$28.00</span></p>
    </article>
  </div>

  <hr class="section-rule">
</section>
</body>
</html>
```